Fitness & sports performance company needs a landing page design

Looking for a landing page for a fitness & sports performance company based in South Florida. The company is 'The Larkfield Fitness Studio', and 'The Larkfield' for short. The main objective of the landing page is to generate leads, and show potential clients the services we offer, as well as pricing for each service. While we are based in South Florida, we also offer online services such as an online trainer and online strength & conditioning programs. Would like to see designs that utilize the colors in our logo.

Target Market(s)

those looking to lose weight, gain strength and make overall healthy lifestyle changes

Font styles to use
Sans Serif

Colors
60b9df
57b5de

Requirements
Must have
• a place to list testimonials, list of services provided, show pricing for each service, colors of the website matching colors in the logo
Nice to have
• i would like to see a landing page that can be utilized to create leads and an email list

```html
<!DOCTYPE html>
<html lang="en">
<head>
<meta charset="utf-8">
<title>The Larkfield Fitness Studio</title>
<link rel="stylesheet" href="https://fonts.googleapis.com/css2?family=Montserrat:wght@400;500;600;700&display=swap">
<style>
  :root {
    --page-bg: #d3ecf7;
    --stripe: #a9dceb;
    --brand: #57b5de;
    --brand-deep: #3fb3cc;
    --pill: #45bad3;
    --ink: #0e3442;
    --card: #f4fbfe;
    --card-edge: #8fd0e6;
    --footer-line: #1f6f86;
    --field: #ffffff;
  }
  * { margin: 0; padding: 0; box-sizing: border-box; }
  html, body { width: 1200px; height: 774px; overflow: hidden; }
  body {
    font-family: "Montserrat", sans-serif;
    color: var(--ink);
    background: #ffffff;
  }
  .landing {
    position: relative;
    width: 1200px;
    height: 774px;
    background: var(--page-bg);
    overflow: hidden;
  }
  .corner-stripe { position: absolute; left: 0; top: 0; }

  .brand-mark {
    position: absolute;
    left: 520px; top: 70px;
    width: 160px; height: 160px;
    border-radius: 50%;
    background: var(--brand);
    display: flex; align-items: center; justify-content: center;
    text-align: center;
  }
  .brand-mark__name {
    font-weight: 700;
    font-size: 22px;
    line-height: 1.1;
    color: #ffffff;
  }

  .title-pill {
    position: absolute;
    left: 430px; top: 262px;
    width: 340px; height: 60px;
    border-radius: 14px;
    background: var(--pill);
    text-align: center;
    padding-top: 7px;
  }
  .title-pill__name { font-weight: 600; font-size: 25px; line-height: 1.2; }
  .title-pill__tag { font-weight: 500; font-size: 11px; letter-spacing: 1px; text-transform: uppercase; }

  .signup {
    position: absolute;
    left: 380px; top: 338px;
    width: 440px; height: 40px;
    display: flex; gap: 8px;
  }
  .signup__field {
    flex: 1;
    height: 40px;
    border: 2px solid var(--card-edge);
    border-radius: 10px;
    background: var(--field);
    padding: 0 14px;
    font-family: "Montserrat", sans-serif;
    font-size: 14px;
    color: var(--ink);
  }
  .signup__field::placeholder { color: #5d8796; }
  .signup__button {
    width: 150px; height: 40px;
    border: 0;
    border-radius: 10px;
    background: var(--ink);
    color: #ffffff;
    font-family: "Montserrat", sans-serif;
    font-weight: 600;
    font-size: 14px;
  }

  .section-pill {
    position: absolute;
    left: 490px;
    width: 220px; height: 36px;
    border-radius: 12px;
    background: var(--pill);
    font-weight: 600; font-size: 20px;
    display: flex; align-items: center; justify-content: center;
  }
  .section-pill--services { top: 398px; }
  .section-pill--testimonials { top: 528px; }

  .services {
    position: absolute;
    left: 65px; top: 446px;
    width: 1070px;
    display: flex; justify-content: space-between;
    list-style: none;
  }
  .service {
    width: 230px; height: 68px;
    border-radius: 14px;
    background: var(--pill);
    display: flex; flex-direction: column;
    align-items: center; justify-content: center;
    text-align: center;
  }
  .service__name { font-weight: 500; font-size: 18px; line-height: 1.12; }
  .service__price { font-weight: 600; font-size: 12px; margin-top: 3px; }

  .testimonials {
    position: absolute;
    left: 65px; top: 576px;
    width: 1070px;
    display: flex; justify-content: space-between;
  }
  .testimonial {
    width: 310px; height: 92px;
    background: var(--card);
    border: 2px solid var(--card-edge);
    padding: 10px 14px;
    font-size: 11px; line-height: 1.4;
    display: flex; flex-direction: column; justify-content: space-between;
  }
  .testimonial__author { align-self: flex-end; font-weight: 600; font-style: normal; }

  .site-footer {
    position: absolute;
    left: 0; top: 682px;
    width: 1200px; height: 48px;
    background: var(--brand-deep);
    border-top: 3px solid var(--footer-line);
    display: flex; align-items: center; justify-content: center;
    font-weight: 600; font-size: 19px;
  }
</style>
</head>
<body>
<main class="landing">
  <svg class="corner-stripe" width="300" height="260" viewBox="0 0 300 260" aria-hidden="true">
    <polygon points="120,0 250,0 0,250 0,120" fill="var(--stripe)"/>
  </svg>

  <div class="brand-mark"><span class="brand-mark__name">The<br>Larkfield</span></div>

  <header class="title-pill">
    <h1 class="title-pill__name">The Larkfield</h1>
    <p class="title-pill__tag">Fitness Studio</p>
  </header>

  <form class="signup" action="#" method="post">
    <input class="signup__field" type="email" name="email" placeholder="Your email for a free session" aria-label="Email address">
    <button class="signup__button" type="submit">Get Started</button>
  </form>

  <h2 class="section-pill section-pill--services">Services</h2>
  <ul class="services">
    <li class="service"><span class="service__name">Sports</span><span class="service__price">from $120 / month</span></li>
    <li class="service"><span class="service__name">Fitness</span><span class="service__price">from $90 / month</span></li>
    <li class="service"><span class="service__name">Strength &amp;<br>Conditioning</span><span class="service__price">from $140 / month</span></li>
    <li class="service"><span class="service__name">Online Training</span><span class="service__price">from $60 / month</span></li>
  </ul>

  <h2 class="section-pill section-pill--testimonials">Testimonials</h2>
  <section class="testimonials">
    <blockquote class="testimonial">
      <p>Coaches here helped me drop the extra weight and build real strength.</p>
      <cite class="testimonial__author">— Maria Lopez</cite>
    </blockquote>
    <blockquote class="testimonial">
      <p>Great team that keeps me motivated, workouts are well planned and fun to follow.</p>
      <cite class="testimonial__author">— Jake Moreno</cite>
    </blockquote>
    <blockquote class="testimonial">
      <p>The online training program is great for busy weeks, simple and flexible to fit my schedule.</p>
      <cite class="testimonial__author">— Ana Ruiz</cite>
    </blockquote>
  </section>

  <footer class="site-footer">Fitness | Sports | Performance Center</footer>
</main>
</body>
</html>
```